Business Card Design for Orthopaedic Surgeon

This is a double-sided glossy business card. I prefer baby blue, teal, and green as color schemes. I have my logo already (many colors that you can choose from). I have photos and examples of my old card (very bland but has the information in it). I also have one that my assistant tried to design, but the writing is too small and I don't love the formatting. But it is close!
I would like my logo to be on the business card but I'm uploading my logo in many different colors so you can choose which one looks best based on the color scheme. I also uploaded many sized headshots so you can choose the best resolution one.

Additional information:
Correct business address:
4382 NW 58th Lane, Suite 305
Tamarac, FL 33417

Everything else on both business cards are accurate.

I actually need 2 different business cards generated. One that includes my cell phone number-- Personal cell: 585-314-9062 in addition to Office phone: (954) 316-4870 and Office Fax: 954-316-4881. Again, one card would have my personal cell and one wouldn't

Overall I just think the baby blue card (uploaded) is missing something on the front--of course it is also missing my office phone/fax/personal cell. I do want my website on the front too. Email: info@wellsorthocare.example

You can use your discretion about what goes on the front vs. what goes on the back to eliminated clutter.

Oh and on the back, I would like to list "Conditions Treated" (not specialties include). The list is:
Carpal Tunnel
Trigger Finger
Ganglion Cysts
Hand Tumors
Han & Wrist Arthritis
Hand, Wrist & Elbow Tendonitis
Fractures of the Hand, Wrist, Elbow and Humerus
Nerve Injuries of the Hand, Wrist & Elbow
Microsurgery
Wrist Arthroscopy
Endoscopic Surgery

Target Market(s)

Primary care doctors, Lawyers, patients

Industry/Entity Type

Medical

Contact Information for Business Card

Please see above in project description

Colors

Designer to choose colors to be used in the design.

Requirements
Must have
• -Correct office info, Board Certified Orthopaedic Hand & Upper Extremity Surgeon
Nice to have
• Something that is classy and wow!

```html
<!DOCTYPE html>
<html lang="en">
<head>
<meta charset="utf-8">
<title>Wells Hand – Business Card</title>
<link rel="stylesheet" href="https://fonts.googleapis.com/css2?family=Didact+Gothic&family=Montserrat:wght@500&display=swap">
<style>
  :root {
    --stage: #b9b9b7;
    --stage-light: #d6d6d3;
    --navy: #0b1f2b;
    --gold: #c8a96a;
    --gold-soft: #e3cfa0;
    --paper: #ffffff;
    --ink: #0b1f2b;
    --text-light: #f2f2f0;
  }
  * { box-sizing: border-box; margin: 0; padding: 0; }
  html, body { width: 1200px; height: 801px; overflow: hidden; }
  body {
    background: radial-gradient(ellipse at 40% 20%, var(--stage-light), var(--stage));
    font-family: "Didact Gothic", "Century Gothic", sans-serif;
    position: relative;
  }
  .card {
    position: absolute;
    width: 540px;
    height: 309px;
    box-shadow: 0 10px 28px rgba(0,0,0,.28);
    overflow: hidden;
  }
  /* Front */
  .card--front { left: 50px; top: 90px; background: var(--paper); }
  .brand {
    position: absolute;
    display: flex;
    align-items: center;
    gap: 10px;
    color: var(--gold);
    font-family: "Montserrat", sans-serif;
    font-weight: 500;
    letter-spacing: 4px;
  }
  .brand__dot {
    border: 3px solid var(--gold);
    border-radius: 50%;
  }
  .card--front .brand { right: 36px; top: 40px; font-size: 20px; }
  .card--front .brand__dot { width: 46px; height: 46px; }
  .address {
    position: absolute;
    right: 36px;
    top: 206px;
    width: 200px;
    text-align: right;
    color: var(--ink);
    font-style: normal;
    font-size: 13px;
    line-height: 1.5;
  }
  .address svg { vertical-align: -2px; margin-left: 4px; }
  .headshot {
    position: absolute;
    left: 34px;
    top: 26px;
    width: 90px;
    height: 90px;
    border-radius: 50%;
    border: 3px solid var(--navy);
    background: radial-gradient(circle at 50% 45%, #3a2a24 0 35%, var(--gold-soft) 36%);
  }
  .name-band {
    position: absolute;
    left: 0;
    top: 124px;
    width: 350px;
    height: 36px;
    background: var(--navy);
    clip-path: polygon(0 0, 100% 0, 92% 100%, 0 100%);
    display: flex;
    align-items: center;
    padding-left: 34px;
  }
  .name {
    font-family: "Montserrat", sans-serif;
    font-weight: 500;
    color: var(--gold);
    font-size: 22px;
    letter-spacing: 1.5px;
  }
  .credentials {
    position: absolute;
    left: 34px;
    top: 168px;
    color: var(--ink);
    font-size: 13px;
    line-height: 1.3;
  }
  .contacts {
    position: absolute;
    left: 34px;
    top: 208px;
    list-style: none;
    color: var(--ink);
    font-size: 12px;
    line-height: 1.42;
  }
  .contacts li { display: flex; align-items: center; gap: 7px; }
  .contacts svg { width: 11px; height: 11px; flex: none; }

  /* Back */
  .card--back { left: 610px; top: 400px; background: var(--navy); }
  .card--back .brand { right: 30px; top: 40px; font-size: 18px; }
  .card--back .brand__dot { width: 40px; height: 40px; }
  .conditions { position: absolute; left: 30px; top: 96px; }
  .conditions__title {
    font-family: "Montserrat", sans-serif;
    font-weight: 500;
    color: var(--gold);
    font-size: 19px;
    letter-spacing: 1px;
    margin-bottom: 6px;
  }
  .conditions__list {
    list-style: none;
    color: var(--text-light);
    font-size: 11.5px;
    line-height: 1.32;
  }
  .conditions__list li::before {
    content: "•";
    color: var(--gold);
    margin-right: 5px;
  }
</style>
</head>
<body>

<section class="card card--front" aria-label="Business card front">
  <div class="brand"><span class="brand__dot"></span><span>WELLS HAND</span></div>

  <address class="address">
    4382 NW 58th Lane, Suite 305
    <svg width="10" height="12" viewBox="0 0 10 12" aria-hidden="true"><path d="M5 0a4 4 0 0 0-4 4c0 3 4 8 4 8s4-5 4-8a4 4 0 0 0-4-4z" fill="#0b1f2b"/><circle cx="5" cy="4" r="1.5" fill="#fff"/></svg><br>
    Tamarac, FL 33417
  </address>

  <div class="headshot" role="img" aria-label="Headshot of the surgeon"></div>

  <div class="name-band"><h1 class="name">RENATA WELLS, MD.</h1></div>

  <p class="credentials">Board Certified Orthopaedic<br>Hand &amp; Upper Extremity Surgeon</p>

  <ul class="contacts">
    <li><svg viewBox="0 0 11 11" aria-hidden="true"><rect x="2.5" y="0.5" width="6" height="10" rx="1" fill="none" stroke="#0b1f2b"/></svg>585-314-9062</li>
    <li><svg viewBox="0 0 11 11" aria-hidden="true"><path d="M2 1l2 0 1 2.5-1.3 1a6 6 0 0 0 2.8 2.8l1-1.3 2.5 1v2a1 1 0 0 1-1 1A9 9 0 0 1 1 2a1 1 0 0 1 1-1z" fill="#0b1f2b"/></svg>(954) 316-4870</li>
    <li><svg viewBox="0 0 11 11" aria-hidden="true"><rect x="3" y="0.5" width="5" height="3" fill="#0b1f2b"/><rect x="0.5" y="4" width="10" height="5" rx="1" fill="#0b1f2b"/><rect x="3" y="7" width="5" height="3.5" fill="#fff" stroke="#0b1f2b"/></svg>954-316-4881</li>
    <li><svg viewBox="0 0 11 11" aria-hidden="true"><rect x="0.5" y="2" width="10" height="7" fill="#0b1f2b"/><path d="M0.5 2l5 4 5-4" fill="none" stroke="#fff"/></svg>info@wellsorthocare.example</li>
    <li><svg viewBox="0 0 11 11" aria-hidden="true"><circle cx="5.5" cy="5.5" r="5" fill="#0b1f2b"/><path d="M0.5 5.5h10M5.5 0.5v10" stroke="#fff" stroke-width=".7"/><ellipse cx="5.5" cy="5.5" rx="2.2" ry="5" fill="none" stroke="#fff" stroke-width=".7"/></svg>www.wellsorthocare.example</li>
  </ul>
</section>

<section class="card card--back" aria-label="Business card back">
  <div class="brand"><span class="brand__dot"></span><span>WELLS HAND</span></div>

  <div class="conditions">
    <h2 class="conditions__title">CONDITIONS TREATED:</h2>
    <ul class="conditions__list">
      <li>Carpal Tunnel</li>
      <li>Trigger Finger</li>
      <li>Ganglion Cysts</li>
      <li>Hand Tumors</li>
      <li>Han &amp; Wrist Arthritis</li>
      <li>Hand, Wrist &amp; Elbow Tendonitis</li>
      <li>Fractures of the Hand, Wrist, Elbow and Humerus</li>
      <li>Nerve Injuries of the Hand, Wrist &amp; Elbow</li>
      <li>Microsurgery</li>
      <li>Wrist Arthroscopy</li>
      <li>Endoscopic Surgery</li>
    </ul>
  </div>
</section>

</body>
</html>
```